Design some Business Cards

Hello! Just need a nice looking business card. I'm looking for something very visual and photographic. My company is a video production company. I will request the PSD files once the project is awarded. Thank you! (Please see attached my current business card with my infos) I also attached a business card I copied from the internet for some inspiration, but please surprise me ;-)

```html
<!DOCTYPE html>
<html lang="en">
<head>
<meta charset="utf-8">
<title>Halo Films – Business Cards</title>
<link rel="stylesheet" href="https://fonts.googleapis.com/css2?family=Quicksand:wght@300;400;700&family=Libre+Baskerville:wght@700&display=swap">
<style>
  :root {
    --backdrop: #8c8c8c;
    --card-dark: #000000;
    --card-light: #ffffff;
    --ink: #111111;
    --ink-soft: #3a3a3a;
    --paper-text: #ffffff;
    --lens-inner: #262626;
    --lens-outer: #000000;
  }
  * { margin: 0; padding: 0; box-sizing: border-box; }
  html, body { width: 1200px; height: 900px; overflow: hidden; }
  body {
    background: radial-gradient(circle at 45% 55%, #a9a9a9 0%, var(--backdrop) 75%);
    font-family: "Quicksand", sans-serif;
    position: relative;
  }
  .card {
    position: absolute;
    width: 560px;
    height: 320px;
    box-shadow: 0 10px 24px rgba(0,0,0,0.35);
  }
  /* Front */
  .card-front {
    left: 560px; top: 80px;
    background: var(--card-dark);
    overflow: hidden;
  }
  .lens-area {
    position: absolute;
    right: -60px; top: -70px;
    width: 290px; height: 290px;
    border-radius: 50%;
    background: radial-gradient(circle at 50% 50%, var(--lens-inner) 0%, #161616 45%, var(--lens-outer) 72%);
  }
  .front-brand {
    position: absolute;
    left: 170px; top: 130px;
    display: flex; align-items: center; gap: 16px;
  }
  .brand-square {
    width: 40px; height: 40px;
    border: 1.5px solid var(--paper-text);
  }
  .brand-name {
    font-family: "Libre Baskerville", serif;
    font-weight: 700;
    font-size: 22px;
    letter-spacing: 0.5px;
    color: var(--paper-text);
  }
  /* Back */
  .card-back {
    left: 90px; top: 470px;
    background: var(--card-light);
    color: var(--ink);
  }
  .holder {
    position: absolute; left: 38px; top: 44px;
  }
  .holder-name {
    font-size: 28px; line-height: 1;
    font-weight: 300; letter-spacing: -0.3px;
  }
  .holder-name strong { font-weight: 700; }
  .holder-role {
    font-size: 12px; font-weight: 400; color: var(--ink-soft);
    margin-top: 4px;
  }
  .divider {
    position: absolute; left: 160px; top: 120px;
    width: 360px; height: 1.5px; background: var(--ink);
  }
  .back-brand {
    position: absolute; right: 40px; top: 40px;
    display: flex; flex-direction: column; align-items: center; gap: 8px;
  }
  .back-brand .brand-square { border-color: var(--ink); width: 64px; height: 50px; }
  .back-brand .brand-name { color: var(--ink); font-size: 17px; }
  .contacts {
    position: absolute; left: 38px; top: 140px;
    list-style: none;
  }
  .contacts li, .socials li {
    display: flex; align-items: center; gap: 10px;
    font-size: 13px; height: 24px;
  }
  .icon {
    width: 17px; height: 17px; border-radius: 50%;
    background: var(--ink); flex: none;
    display: flex; align-items: center; justify-content: center;
  }
  .socials {
    position: absolute; right: 40px; top: 220px;
    list-style: none;
  }
  .socials li { justify-content: flex-end; height: 30px; font-size: 14px; }
  .socials .icon { width: 20px; height: 20px; }
</style>
</head>
<body>
  <section class="card card-front">
    <div class="lens-area" role="img" aria-label="Soft dark camera lens graphic"></div>
    <div class="front-brand">
      <span class="brand-square"></span>
      <span class="brand-name">HALO FILMS</span>
    </div>
  </section>

  <section class="card card-back">
    <div class="holder">
      <p class="holder-name"><strong>Lucien</strong> Marchand</p>
      <p class="holder-role">Professional Photographer</p>
    </div>
    <div class="divider"></div>

    <div class="back-brand">
      <span class="brand-square"></span>
      <span class="brand-name">HALO FILMS</span>
    </div>

    <ul class="contacts">
      <li>
        <span class="icon">
          <svg width="10" height="10" viewBox="0 0 24 24"><path fill="#fff" d="M6.6 10.8a15.1 15.1 0 0 0 6.6 6.6l2.2-2.2c.3-.3.7-.4 1-.2 1.1.4 2.3.6 3.6.6.6 0 1 .4 1 1V20c0 .6-.4 1-1 1A17 17 0 0 1 3 4c0-.6.4-1 1-1h3.5c.6 0 1 .4 1 1 0 1.3.2 2.5.6 3.6.1.3 0 .7-.2 1z"/></svg>
        </span>
        555.210.4836
      </li>
      <li>
        <span class="icon">
          <svg width="10" height="10" viewBox="0 0 24 24"><path fill="#fff" d="M2 5h20v14H2z"/><path fill="none" stroke="#111" stroke-width="2" d="M2 5l10 8 10-8"/></svg>
        </span>
        lmarchand@halofilms.com
      </li>
      <li>
        <span class="icon"></span>
        plus.halofilms.com
      </li>
    </ul>

    <ul class="socials">
      <li>page.halofilms.com <span class="icon"></span></li>
      <li>video.halofilms.com <span class="icon"></span></li>
    </ul>
  </section>
</body>
</html>
```